Business Card Design for Event Planning Company

Create a business card for event planning company using our new logo. After I pick the design, I will need files made for 6 employees. Our company provides event design & logistics services as well as venue management. The font should be sans serif and complementary to the logo. I will need to know the name of the font selected for the final design. The phone numbers listed should be separated by "." not "-"

Address for the card
PO Box 218, Washington, DC 20019

Card One
Lorna Pettigrew
lpettigrew@galaplanora.com
202.481.7032

Card Two
Marisol Dunleavy
mdunleavy@galaplanora.com
202.416.2950

Card Three
Rebecca Vasquetti
rvasquetti@galaplanora.com
978.527.6043

Card Four
Tessa Brink
tbrink@galaplanora.com
202.458.1276

Card Five
Ada-Rose Pemberton-Nwaku
adarose@galaplanora.com
202.819.3047

Card Six
Valerie Thornbury
Valerie@galaplanora.com
202.592.8134

Target Market(s)

Corporate/Non-Profit

Industry/Entity Type

Event Planning

Contact Information for Business Card

Address for the card

Card One
Lorna Pettigrew
lpettigrew@galaplanora.com
202.481.7032

Card Two
Marisol Dunleavy
202.416.2950

Card Three
Rebecca Vasquetti
978.527.6043

Card Four
Tessa Brink
tbrink@galaplanora.com
202.458.1276

Card Five
Ada-Rose Pemberton-Nwaku
202.819.3047

Card Six
Valerie Thornbury
202.592.8134

Font styles to use
Sans Serif

Colors

Designer to choose colors to be used in the design.

Requirements
Must have
• Two-sided with logo
Should not have
• Extra colors or be too busy

```html
<!DOCTYPE html>
<html lang="en">
<head>
<meta charset="utf-8">
<title>Gala Planora – Business Card</title>
<link href="https://fonts.googleapis.com/css2?family=Work+Sans:wght@300;400;700&display=swap" rel="stylesheet">
<style>
  :root {
    --backdrop: #2a2421;
    --card: #1b1b1c;
    --card-edge: #262627;
    --silver: #b9b9bb;
    --white: #f4f4f4;
    --teal: #5fa8a8;
    --rule: #5a5a5c;
  }
  * { box-sizing: border-box; margin: 0; padding: 0; }
  html, body {
    width: 1200px; height: 715px; overflow: hidden;
    background: var(--backdrop);
    font-family: "Work Sans", Arial, sans-serif;
  }
  .stage {
    position: relative; width: 1200px; height: 715px;
    display: flex; align-items: center; justify-content: center; gap: 50px;
  }
  .card {
    position: relative; width: 525px; height: 300px;
    background: var(--card);
    border: 1px solid var(--card-edge);
    border-radius: 8px;
    box-shadow: 0 10px 30px rgba(0,0,0,.45);
  }
  /* Front */
  .card--front { display: flex; align-items: center; justify-content: center; }
  .brand { display: flex; align-items: center; gap: 14px; }
  .brand__dot { width: 16px; height: 16px; border-radius: 50%; background: var(--silver); }
  .brand__name {
    font-weight: 300; font-size: 50px; letter-spacing: 0.5px;
    color: var(--silver);
  }
  /* Back */
  .card--back { display: flex; align-items: center; padding: 0 34px 0 40px; }
  .back-brand { display: flex; align-items: center; gap: 10px; width: 190px; }
  .back-brand__dot { width: 12px; height: 12px; border-radius: 50%; background: var(--teal); flex: none; }
  .back-brand__name { font-weight: 300; font-size: 30px; color: var(--teal); }
  .divider { width: 1px; height: 96px; background: var(--rule); margin: 0 24px 0 14px; flex: none; }
  .contact { color: var(--white); font-size: 13.5px; line-height: 1.5; font-weight: 400; }
  .contact__name {
    font-weight: 700; font-size: 19px; letter-spacing: 1px;
    text-transform: uppercase; margin-bottom: 4px; line-height: 1.2;
  }
  .contact__surname { color: var(--teal); }
  .contact__line { display: flex; align-items: center; gap: 8px; }
  .contact__icon { width: 11px; height: 11px; flex: none; }
  .contact__address { margin-bottom: 2px; }
</style>
</head>
<body>
<main class="stage">
  <section class="card card--front" aria-label="Card front">
    <div class="brand">
      <span class="brand__dot"></span>
      <span class="brand__name">galaplanora</span>
    </div>
  </section>

  <section class="card card--back" aria-label="Card back">
    <div class="back-brand">
      <span class="back-brand__dot"></span>
      <span class="back-brand__name">galaplanora</span>
    </div>
    <div class="divider"></div>
    <div class="contact">
      <p class="contact__name">Lorna <span class="contact__surname">Pettigrew</span></p>
      <p class="contact__address">PO Box 218,<br>Washington, DC 20019</p>
      <p class="contact__line">
        <svg class="contact__icon" viewBox="0 0 24 24" aria-hidden="true">
          <path fill="var(--teal)" d="M6.6 10.8a15.1 15.1 0 0 0 6.6 6.6l2.2-2.2a1 1 0 0 1 1-.25 11.4 11.4 0 0 0 3.6.57 1 1 0 0 1 1 1V20a1 1 0 0 1-1 1A17 17 0 0 1 3 4a1 1 0 0 1 1-1h3.5a1 1 0 0 1 1 1c0 1.25.2 2.45.57 3.57a1 1 0 0 1-.25 1z"/>
        </svg>
        202.481.7032
      </p>
      <p class="contact__line">
        <svg class="contact__icon" viewBox="0 0 24 24" aria-hidden="true">
          <rect x="2" y="5" width="20" height="14" rx="1.5" fill="none" stroke="var(--teal)" stroke-width="2.2"/>
          <path d="M3 6l9 7 9-7" fill="none" stroke="var(--teal)" stroke-width="2.2"/>
        </svg>
        lpettigrew@galaplanora.com
      </p>
    </div>
  </section>
</main>
</body>
</html>
```